Life Insurance Landing Page (for lead gen)

We need a high converting life insurance page created. It will be housed at www.CoverageVerifyHub.com. We will be driving former life insurance prospects to this page where they will only need to confirm their phone number & email in order to receive an updated quote.
Updates

Only the page design is required, the coding will be done on our end. 

Target Market(s)

People who have expressed an interest in obtaining life insurance.

Industry/Entity Type

Life Insurance

Requirements
Must have
• 1) Under "CoverageVerifyHub.com" Please include a "Powered by KRBT" tag and match the colors of this site: http://thekrbt.com/life-insurance-services.html to the page.

2) The form should ask for their phone number and include an appointment calendar widget (we'll code the functionality) so they can choose the date/time of their call. It should also have an email confirmation field.

3) the overall message next to the form fields should be "Thanks for visiting Gordon (we'll personalize this "firstname" field ), please let us know the best time to schedule a brief call so we can give you an updated, rock bottom pricing quote on a policy. We'll also email you with the information, please confirm your email here and we'll send you the details.

4) We'd like to include a box that appears to be a personalized "quote briefing" snapshot that will list this information: "Name: _________" "Birth Date:"____________" "Policy Type: _______", "Coverage Amount: ____________" " all these fields will be populated into the page.

```html
<!DOCTYPE html>
<html lang="en">
<head>
<meta charset="utf-8">
<title>CoverageVerifyHub.com – Life Insurance Quote</title>
<link href="https://fonts.googleapis.com/css2?family=Arimo:wght@400;700&family=Lato:wght@400;700&display=swap" rel="stylesheet">
<style>
:root{
  --blue:#1a8fd0;
  --blue-dark:#0c6aa8;
  --blue-deep:#0e5f97;
  --red:#b5121b;
  --field:#efefef;
  --field-line:#c9c9c9;
  --text:#333;
  --muted:#555;
  --white:#fff;
}
*{box-sizing:border-box;margin:0;padding:0}
html,body{width:1174px;height:1200px;overflow:hidden;background:var(--white)}
body{font-family:Arimo,Arial,sans-serif;color:var(--text)}
.page{position:relative;width:1174px;height:1200px;overflow:hidden}
.abs{position:absolute}

.top-bar{left:0;top:0;width:1174px;height:54px;background:linear-gradient(#2b9ee0,#0f78bd)}
.hero{left:0;top:54px;width:1174px;height:459px;
  background:radial-gradient(ellipse at 20% 50%,#2d3f5e 0 14%,transparent 30%),
  radial-gradient(ellipse at 90% 85%,#a9c63a 0 8%,transparent 20%),
  linear-gradient(90deg,#d9d4cc,#b9b3aa 40%,#cfc9bf 70%,#e7e2d8)}

.follow{color:var(--white);font-size:22px;display:flex;align-items:center;gap:6px}
.follow .dot{width:25px;height:25px;border-radius:50%;background:var(--white)}

.logo-badge{left:414px;top:0;width:346px;height:112px}
.logo-name{left:414px;top:22px;width:346px;text-align:center;font-weight:700;font-size:30px;color:var(--blue-dark);letter-spacing:-.5px}
.logo-tag{left:414px;top:76px;width:346px;text-align:center;font-weight:700;font-size:15px;color:var(--red)}

.greeting{left:310px;top:149px;width:270px;height:223px;background:rgba(20,20,20,.88);border-top:4px solid var(--blue);color:var(--white);font-family:Lato,sans-serif;text-align:center}
.greeting h2{font-family:Arimo,sans-serif;font-size:23px;font-weight:700;margin:14px 9px 0;padding-bottom:11px;border-bottom:1px solid #777}
.greeting p{font-size:18.5px;line-height:25.5px;margin-top:10px;padding:0 12px}

.form-panel{left:669px;top:104px;width:367px;height:286px;background:#f6f6f6;border:3px solid var(--white);box-shadow:0 0 6px rgba(0,0,0,.25)}
.panel-head{height:47px;background:linear-gradient(#1e95d6,#0d71b5);color:var(--white);font-weight:700;font-size:28px;line-height:47px;padding-left:69px}
.field{position:absolute;height:33px;background:var(--field);border:1px solid var(--field-line);border-radius:3px;font-size:13px;color:#666;line-height:31px;padding-left:9px}
.field svg{position:absolute;right:8px;top:6px}
.quote-btn{left:853px;top:347px;width:63px;height:30px;border-radius:4px;background:linear-gradient(#e0232c,#a30d15);color:var(--white);font-weight:700;font-size:15px;line-height:30px;text-align:center;white-space:nowrap;overflow:hidden}

.calendar{left:637px;top:319px;width:243px;height:174px;background:var(--white);border:1px solid #ccc;box-shadow:0 2px 6px rgba(0,0,0,.3);font-size:11px}
.calendar::before{content:"";position:absolute;top:-8px;left:167px;border:8px solid transparent;border-top:0;border-bottom-color:var(--white)}
.cal-head{display:flex;justify-content:space-between;align-items:center;padding:8px 8px 6px}
.cal-head b{color:var(--red);font-size:14px}
.cal-arrow{width:17px;height:16px;border:1px solid #bbb;border-radius:2px;font-size:11px;line-height:14px;text-align:center;color:#555}
.calendar table{border-collapse:collapse;margin:0 9px;width:225px}
.calendar th{font-size:10px;color:#555;font-weight:700;height:17px}
.calendar td{text-align:center;height:22px;border-bottom:1px solid #ddd;color:#333}
.calendar td.mark{color:var(--red)}

.slides{left:974px;top:490px;display:flex;gap:6px}
.slides i{width:13px;height:13px;border-radius:50%;background:var(--blue-dark)}
.slides i:first-child{background:var(--red)}

.card{left:138px;width:898px;background:var(--white);box-shadow:0 0 4px rgba(0,0,0,.15)}
.card-head{height:47px;background:linear-gradient(#1e95d6,#0d71b5);color:var(--white);font-weight:700;font-size:24px;line-height:50px;text-align:center}
.briefing{top:526px;height:187px}
.briefing .field{font-size:13px;color:#333;padding-left:12px}
.textarea{height:80px;line-height:19px;padding-top:8px}
.overpay{top:725px;height:139px}
.overpay p{font-size:13px;line-height:19px;text-align:center;padding:8px 10px 0;color:#333}
.read-more{display:block;text-align:center;color:var(--blue-dark);font-weight:700;font-size:13px;margin-top:4px}

.rule{left:138px;width:898px;height:1px;background:#ddd}
.commit-title{left:138px;top:915px;width:898px;text-align:center;color:var(--blue-dark);font-weight:700;font-size:24px}
.commit-lead{left:138px;top:960px;width:898px;text-align:center;font-weight:700;font-size:13px}
.commit-text{left:138px;top:986px;width:898px;text-align:center;font-size:13px;line-height:19px;color:var(--muted)}

.footer{left:0;top:1089px;width:1174px;height:111px;background:var(--blue-deep);color:var(--white);font-family:Lato,sans-serif}
.foot-links{left:138px;top:17px;font-size:13px;font-weight:700}
.foot-links span{margin:0 7px;font-weight:400}
.foot-follow{left:135px;top:45px}
.copy{left:138px;top:85px;font-size:13px;letter-spacing:.3px}
.disclaimer{left:543px;top:14px;width:495px}
.disclaimer h3{font-family:Arimo,sans-serif;font-size:19px;font-weight:400;padding-bottom:6px;border-bottom:1px solid #3d8cc4}
.disclaimer p{font-size:12.5px;line-height:16px;margin-top:9px;letter-spacing:.3px}
</style>
</head>
<body>
<div class="page">
  <div class="abs top-bar"></div>
  <div class="abs hero" role="img" aria-label="Photo of a smiling businessman in a suit with arms folded, in a softly blurred office"></div>

  <div class="abs follow" style="left:139px;top:15px">Follow Us <i class="dot"></i><i class="dot"></i><i class="dot"></i><i class="dot"></i></div>

  <svg class="abs logo-badge" viewBox="0 0 346 112" aria-hidden="true">
    <path d="M1 0V82L173 111L345 82V0Z" fill="#fff" stroke="#d5d5d5"/>
    <line x1="14" y1="67" x2="332" y2="67" stroke="#e0e0e0"/>
  </svg>
  <div class="abs logo-name">CoverageVerifyHub.com</div>
  <div class="abs logo-tag">Powered by KRBT</div>

  <div class="abs greeting">
    <h2>"Hey Martin"</h2>
    <p>Thank you for you interest, here is your policy briefing, just confirm your phone number and email and we'll get you the details.</p>
  </div>

  <div class="abs form-panel">
    <div class="panel-head">Start Here</div>
  </div>
  <div class="field" style="left:682px;top:166px;width:339px">Phone Number</div>
  <div class="field" style="left:682px;top:211px;width:339px">Appointment
    <svg width="20" height="19" viewBox="0 0 20 19"><rect x="1" y="3" width="18" height="15" fill="none" stroke="#555" stroke-width="1.6"/><rect x="1" y="3" width="18" height="4" fill="#555"/><path d="M5 10h2M9 10h2M13 10h2M5 14h2M9 14h2M13 14h2" stroke="#555" stroke-width="2"/></svg>
  </div>
  <div class="field" style="left:682px;top:255px;width:339px">Email Address</div>
  <div class="field" style="left:682px;top:293px;width:155px">Date
    <svg width="20" height="19" viewBox="0 0 20 19"><rect x="1" y="3" width="18" height="15" fill="none" stroke="#555" stroke-width="1.6"/><rect x="1" y="3" width="18" height="4" fill="#555"/><path d="M5 10h2M9 10h2M13 10h2M5 14h2M9 14h2M13 14h2" stroke="#555" stroke-width="2"/></svg>
  </div>
  <div class="field" style="left:865px;top:293px;width:155px">Time
    <svg width="21" height="21" viewBox="0 0 21 21" style="top:5px"><circle cx="10.5" cy="12" r="8" fill="none" stroke="#444" stroke-width="2"/><path d="M8 2h5M10.5 12V7" stroke="#444" stroke-width="2"/></svg>
  </div>
  <div class="abs quote-btn">Get Quote</div>

  <div class="abs calendar">
    <div class="cal-head"><span class="cal-arrow">←</span><b>February 2014</b><span class="cal-arrow">→</span></div>
    <table>
      <tr><th>SUN</th><th>MON</th><th>TUE</th><th>WED</th><th>THU</th><th>FRI</th><th>SAT</th></tr>
      <tr><td></td><td></td><td></td><td></td><td></td><td></td><td>1</td></tr>
      <tr><td>2</td><td>3</td><td>4</td><td>5</td><td>6</td><td class="mark">7</td><td>8</td></tr>
      <tr><td>9</td><td>10</td><td>10</td><td>12</td><td>13</td><td>14</td><td>15</td></tr>
      <tr><td>16</td><td>17</td><td>18</td><td>19</td><td>20</td><td>21</td><td>22</td></tr>
      <tr><td>23</td><td>24</td><td>25</td><td>26</td><td>27</td><td>28</td><td></td></tr>
    </table>
  </div>

  <div class="abs slides"><i></i><i></i><i></i></div>

  <section class="abs card briefing">
    <div class="card-head">Policy Briefing</div>
  </section>
  <div class="field" style="left:147px;top:587px;width:301px">Lorem ipsum dol</div>
  <div class="field" style="left:455px;top:587px;width:302px">Lorem ipsum dol</div>
  <div class="field" style="left:762px;top:587px;width:265px;padding-left:29px;color:#333">$25.000
    <svg width="22" height="20" viewBox="0 0 22 20" style="top:6px;right:6px"><rect width="22" height="20" fill="#ccc"/><path d="M5 7h12l-6 7z" fill="#666"/></svg>
  </div>
  <div class="field textarea" style="left:147px;top:625px;width:500px;color:#333;padding-left:12px">Lorem ipsum dolor sit amet, consectetur adipisicing elit, sed do eiusmod tempor incididunt ut labore et dolore magna aliqua. Ut enim ad minim veniam, quis nostrud laboris nisi ut aliquip ex ea commodo consequat.</div>
  <div class="field" style="left:657px;top:634px;width:164px">Martin</div>
  <div class="field" style="left:829px;top:634px;width:198px">06/04/1980
    <svg width="20" height="19" viewBox="0 0 20 19"><rect x="1" y="3" width="18" height="15" fill="none" stroke="#777" stroke-width="1.6"/><rect x="1" y="3" width="18" height="4" fill="#777"/><path d="M5 10h2M9 10h2M13 10h2M5 14h2M9 14h2M13 14h2" stroke="#777" stroke-width="2"/></svg>
  </div>
  <div class="field" style="left:657px;top:672px;width:164px">Ut enim ad minim</div>
  <div class="field" style="left:829px;top:672px;width:198px">345 6578</div>

  <section class="abs card overpay">
    <div class="card-head">Are You Overpaying?</div>
    <p>Having the right life insurance is pivotal in planning for the future of you and your loved ones. Life insurance can help solve a lot of the problems your family would be faced with should the unexpected happen. Don't leave the future of you and your loved ones to chance. Keystone Ridge Benefit Services can help you find the right life insurance coverage for you, and help ensure that your policy continually meets your needs.</p>
    <span class="read-more">Read More »</span>
  </section>

  <div class="abs rule" style="top:899px"></div>
  <h2 class="abs commit-title">Our Commitment</h2>
  <div class="abs rule" style="top:948px"></div>
  <p class="abs commit-lead">We Stand Behind Our Commitment to do our Best to get You the Lowest Rates Online. Getting a cheap car insurance quote is so easy now.</p>
  <p class="abs commit-text">We believe in providing exceptional customer service. At Coverage Verify Hub, we believe in having the best of both worlds. Low rates, excellent coverage and local reps that are there every step of the way. This is what sets Coverage Verify Hub apart from our competition. And that's what makes us the obvious choice when it comes to your car insurance needs.</p>
  <div class="abs rule" style="top:1056px"></div>

  <footer class="abs footer">
    <div class="abs foot-links">Contact Us<span>|</span>Privacy &amp; Security<span>|</span>Terms of Use<span>|</span>Opt-out</div>
    <div class="abs follow foot-follow">Follow Us : <i class="dot"></i><i class="dot"></i><i class="dot"></i><i class="dot"></i></div>
    <div class="abs copy">Copyright 2014 CoverageVerifyHub.</div>
    <div class="abs disclaimer">
      <h3>Disclaimer</h3>
      <p>Lorem ipsum dolor sit amet, consectetur adipisicing elit, sed do eiusmod tempor incididunt ut labore et dolore magna aliqua. Ut enim ad minim veniam, quis nostrud laboris nisi ut aliquip ex ea commodo consequat.</p>
    </div>
  </footer>
</div>
</body>
</html>
```